2 x Digitize Logo | 2 x Business Cards | 2 x Fridge Magnets

We require 6 deliverables:
1. Residential logo redrawn (same just high quality for large print format).
2. Corporate logo redrawn (minor changes to wording and high quality for large print format).
3. New business card design for Furniture Removals (residential)
4. New business card design for Corporate Relocations (business)
5. New Fridge magnet for Furniture removals (residential)
6. New fridge magnet for Corporate Relocations (business)
1. Residential Logo
a. We require the logo to be translated into a high quality digital image with no modifications.
(see attached resilogo.jpg)
2. Residential Logo
a. We require the logo to be edited (add the word corporate relocations) be translated into a high quality digital image.
(see attached corplogo.jpg)
3. Using the resilogo please make a new business card for our business.
a. Please see the web site https://www.bluegatehaulage.com.au for colours and inspiration.
b. The residential business card needs the following information:
i. Business Name (using the residential logo).
ii. Free Call: 1800 BG Haul (the B, G and Haul much be the same colour as the logo).
iii. Website: www.BluegateHaulage.com.au
iv. Address: 4/6 Marlow Court, VIC 3201
v. Email: move@BluegateHaulage.com.au
vi. backof Card:
Review our service
www.TellTallyHub.com.au
Services: Local, Country, Interstate | Furniture Removals | Piano, Billiard Tables & Antiques
4. Using the corplogo please make a new business card for our business.
b. The corporate business card needs the following information:
i. Business Name (using the corporate logo).
v. Email: corporate@BluegateHaulage.com.au
vi. Back of Card:
Review our service
www.TellTallyHub.com.au
Services: Corporate relocations | Office equipment moves | Packing Service | Packing Materials
5. Using the resilogo please make a new fridge magent for our business.
b. The residential fidge magnet needs the following information:
iv. Services: Local, Country, Interstate | Furniture Removals | Piano, Billiard Tables & Antiques
6. Using the corplogo please make a new fridge magent for our business.
b. The corporate fidge magnet needs the following information:
iv. Services: Local, Country, Interstate | Corporate relocations
Target Market(s)
Residential Furniture Removals and Corporate Office relocations
Industry/Entity Type
Business
Contact Information for Business Card
Please see full brief for six items required
Requirements
Must have
- Clean simple, easy to read
Nice to have
- fresh, stand out, eye catching
Should not have
- plain, standard, boring, general

```html
<!DOCTYPE html>
<html lang="en">
<head>
<meta charset="utf-8">
<title>Bluegate Haulage – Corporate Business Card</title>
<link rel="stylesheet" href="https://fonts.googleapis.com/css2?family=Source+Sans+3:wght@400;600&display=swap">
<style>
  :root {
    --brand-green: #0b7a3b;
    --brand-red: #c8202a;
    --card-white: #f6f6f6;
    --ink: #1f1f1f;
    --page: #e6e6e6;
    --on-green: #ffffff;
  }
  * { box-sizing: border-box; margin: 0; padding: 0; }
  html, body {
    width: 1200px; height: 900px; overflow: hidden;
    background: var(--page);
    font-family: "Source Sans 3", "Myriad Pro", Arial, sans-serif;
  }
  .business-card {
    position: absolute; left: 75px; top: 125px;
    width: 1050px; height: 650px;
    background: linear-gradient(135deg, #ffffff 0%, var(--card-white) 60%, #ececec 100%);
    box-shadow: 0 10px 30px rgba(0,0,0,0.18);
    overflow: hidden;
  }
  .card-panel { position: absolute; inset: 0; width: 1050px; height: 650px; }
  .services {
    position: absolute; left: 64px; top: 258px;
    color: var(--on-green);
  }
  .services-title { font-size: 30px; font-weight: 400; letter-spacing: 0.5px; margin-bottom: 28px; }
  .services-list { list-style: none; font-size: 28px; line-height: 38px; }
  .services-list li { position: relative; padding-left: 30px; }
  .services-list li::before {
    content: ""; position: absolute; left: 0; top: 11px;
    width: 18px; height: 18px; border-radius: 50%; background: var(--on-green);
  }
  .review {
    position: absolute; left: 60px; top: 518px;
    color: var(--on-green); font-size: 28px; line-height: 42px;
  }
  .brand {
    position: absolute; left: 560px; top: 150px; width: 440px;
    display: flex; align-items: center; justify-content: center; gap: 16px;
  }
  .brand-dot { width: 26px; height: 26px; border-radius: 50%; background: var(--brand-red); flex: none; }
  .brand-name {
    color: var(--brand-green); font-size: 44px; font-weight: 600;
    letter-spacing: 1px; white-space: nowrap;
  }
  .contact {
    position: absolute; right: 38px; top: 424px;
    list-style: none; text-align: right; color: var(--ink);
    font-size: 27px; line-height: 38px;
  }
  .contact li { display: flex; justify-content: flex-end; align-items: center; gap: 8px; }
  .contact li.address { margin-top: 10px; }
  .contact svg { width: 20px; height: 20px; fill: var(--brand-green); flex: none; }
  .hl-red { color: var(--brand-red); font-weight: 600; }
  .hl-green { color: var(--brand-green); font-weight: 600; }
</style>
</head>
<body>
<main class="business-card">
  <svg class="card-panel" viewBox="0 0 1050 650" aria-hidden="true">
    <polygon points="0,0 438,0 319,97 548,650 0,650" fill="var(--brand-green)"/>
    <polyline points="438,0 319,97 548,650" fill="none" stroke="var(--brand-red)" stroke-width="4"/>
  </svg>

  <section class="services">
    <h2 class="services-title">SERVICES</h2>
    <ul class="services-list">
      <li>Corporate relocations</li>
      <li>Office equipment moves</li>
      <li>Packing Service</li>
      <li>Packing Materials</li>
    </ul>
  </section>

  <p class="review">Review our service<br>www.TellTallyHub.com.au</p>

  <div class="brand">
    <span class="brand-dot"></span>
    <span class="brand-name">BLUEGATE HAULAGE</span>
  </div>

  <ul class="contact">
    <li><span>1800 <span class="hl-red">B</span><span class="hl-green">G</span> <span class="hl-red">Haul</span> / 1800 42 85 17</span>
      <svg viewBox="0 0 24 24"><path d="M6.6 10.8a15.1 15.1 0 0 0 6.6 6.6l2.2-2.2c.3-.3.7-.4 1-.2 1.1.4 2.3.6 3.6.6.6 0 1 .4 1 1V20c0 .6-.4 1-1 1A17 17 0 0 1 3 4c0-.6.4-1 1-1h3.5c.6 0 1 .4 1 1 0 1.3.2 2.5.6 3.6.1.3 0 .7-.2 1z"/></svg></li>
    <li><span>corporate@BluegateHaulage.com.au</span>
      <svg viewBox="0 0 24 24"><path d="M2 5h20v14H2z M3.5 6.5 12 13l8.5-6.5z" fill-rule="evenodd"/></svg></li>
    <li><span>www.BluegateHaulage.com.au</span>
      <svg viewBox="0 0 24 24"><circle cx="12" cy="12" r="10"/><path d="M2 12h20M12 2c3 3 3 17 0 20M12 2c-3 3-3 17 0 20" stroke="#fff" stroke-width="1.4" fill="none"/></svg></li>
    <li class="address"><span>4/6 Marlow Court, VIC 3201</span>
      <svg viewBox="0 0 24 24"><path d="M12 2a7 7 0 0 0-7 7c0 5 7 13 7 13s7-8 7-13a7 7 0 0 0-7-7zm0 9.5A2.5 2.5 0 1 1 12 6.5a2.5 2.5 0 0 1 0 5z"/></svg></li>
  </ul>
</main>
</body>
</html>
```